依頼詳細
アルミパッケージ表面のデザインをお願いします。
※サイズはW110×H170mmのチャック付き

アルミ袋は黒色で考えているので、
ロゴのイメージに沿うものでお願いします。

・商品名含むロゴ素材を添付しますので、こちらを使用してください。
※ロゴの配色はそのままか、修正いずれも構いません。

・配合成分は「citrulline 800mg arginine 500mg」を行のトップにして
見やすく配置し、他はバランスを見て、順番を入れ替えても問題ありません。
※添付画像を参考にお願いします。

以下、必須の表記です。

・商品名とロゴ
・サブタイトル「MEN'S SUPPLEMENT」

・配合成分
citrulline 800mg arginine 500mg
zing
maca
tongkat ali
black ginger
ginseng
soft-shelled turtle
black garlic
oystar

・「180tablets」
・「栄養機能食品(亜鉛)」
記載項目
薬機法の表記チェックや印刷前の確認などで、採用させて頂いた後、
最終的な納品までに、何回か細かい修正をお願い場合がございますので、その点をご了承のほどお願い致します。
希望イメージ
シンプル 複雑
単色 カラフル
暗い 明るい
日常 高級
遊び心 厳粛
未来的 伝統的
女性的 男性的
希望する色
納品ファイル
• 高解像度JPG (.jpg)
• イラストレーター形式 (.ai)
• フォトショップ形式 (.psd)
補足説明
最終的な納品の際には、PDFもお願いします。
提案数をもう少し増やした中で選びたいので延長しました。シンプルな配色が一番の希望です。良いものがあった場合は、即決する場合がございます。
■ 選んだ理由

イメージに一番近いものでした。

■ 提案者全員のお礼・コメント

皆様の募集も素晴らしいものでした。ありがとうございました。

```html
<!DOCTYPE html>
<html lang="ja">
<head>
<meta charset="utf-8">
<title>VIGOR CORE – Men's Supplement Pouch</title>
<link href="https://fonts.googleapis.com/css2?family=Cinzel:wght@400;500&family=Montserrat:wght@400;500;600&family=Noto+Sans+JP:wght@700&display=swap" rel="stylesheet">
<style>
  :root {
    --pouch-black: #2a201d;
    --gold: #c9a24f;
    --gold-line: #b8924a;
    --ink-light: #f2ede6;
  }
  html, body {
    margin: 0;
    padding: 0;
    overflow: hidden;
    background: var(--pouch-black);
  }
  .pouch {
    position: relative;
    width: 778px;
    height: 1200px;
    background: var(--pouch-black);
    overflow: hidden;
    font-family: "Montserrat", sans-serif;
    color: var(--ink-light);
  }
  .freshness-note {
    position: absolute;
    top: 32px;
    right: 34px;
    font-size: 10px;
    letter-spacing: 2px;
    color: var(--ink-light);
  }
  .brand-frame {
    position: absolute;
    left: 150px;
    top: 170px;
    width: 482px;
    height: 484px;
    border: 2px solid var(--gold-line);
    box-sizing: border-box;
  }
  .brand-square {
    position: absolute;
    left: 339px;
    top: 252px;
    width: 100px;
    height: 100px;
    border: 3px solid var(--gold);
    box-sizing: border-box;
  }
  .brand-name {
    position: absolute;
    left: 0;
    right: 0;
    top: 430px;
    text-align: center;
    font-family: "Cinzel", serif;
    font-weight: 500;
    font-size: 38px;
    letter-spacing: 2px;
    color: var(--gold);
  }
  .subtitle {
    position: absolute;
    left: 0;
    right: 0;
    top: 752px;
    text-align: center;
    font-family: "Cinzel", serif;
    font-size: 25px;
    letter-spacing: 6px;
    color: var(--gold);
  }
  .divider {
    position: absolute;
    left: 238px;
    top: 808px;
    width: 302px;
    height: 1px;
    background: var(--gold-line);
  }
  .ingredients {
    position: absolute;
    left: 0;
    right: 0;
    top: 832px;
    text-align: center;
    color: var(--ink-light);
  }
  .ingredients-lead {
    font-size: 21px;
    font-weight: 500;
    margin: 0 0 12px;
  }
  .ingredients-list {
    font-size: 14px;
    margin: 0 0 8px;
  }
  .tablet-count {
    position: absolute;
    left: 337px;
    top: 972px;
    width: 104px;
    height: 104px;
    border: 2px solid var(--ink-light);
    border-radius: 50%;
    box-sizing: border-box;
    display: flex;
    flex-direction: column;
    align-items: center;
    justify-content: center;
  }
  .tablet-count-number {
    font-size: 20px;
    font-weight: 600;
    line-height: 1.1;
  }
  .tablet-count-unit {
    font-size: 10px;
    letter-spacing: 1px;
  }
  .food-category {
    position: absolute;
    left: 0;
    right: 0;
    top: 1120px;
    text-align: center;
    font-family: "Noto Sans JP", sans-serif;
    font-weight: 700;
    font-size: 20px;
    letter-spacing: 1px;
    color: var(--ink-light);
  }
</style>
</head>
<body>
  <main class="pouch">
    <p class="freshness-note">STAY FRESH</p>

    <div class="brand-frame"></div>
    <div class="brand-square"></div>
    <h1 class="brand-name">VIGOR CORE</h1>

    <h2 class="subtitle">MEN'S SUPPLEMENT</h2>
    <div class="divider"></div>

    <div class="ingredients">
      <p class="ingredients-lead">citrulline 800mg / arginine 500mg</p>
      <p class="ingredients-list">zing / maca / tongkat ali / black ginger / ginseng</p>
      <p class="ingredients-list">soft-shelled turtle / black garlic / oystar</p>
    </div>

    <div class="tablet-count">
      <span class="tablet-count-number">180</span>
      <span class="tablet-count-unit">TABLETS</span>
    </div>

    <p class="food-category">栄養機能食品(亜鉛)</p>
  </main>
</body>
</html>
```